Brandell Law PLLC updated letterhead for solo law practice - legal/professional services

I need a new letterhead design on a word document for my solo law practice. I have attached my current letterhead. Here is my company info:

Douglas Brandell
Brandell Law PLLC
2750 Whitcombe, Suite 410
Dallas, Texas 75219
Phone: 214 555 0186
Email: douglas@brandell-legal.example
Website: www.brandell-legal.example

Preferably I'd like the logo on top followed by my name and email (in the header)

At the bottom (footer) i'd like the rest of the information.

I am fine using a color for the line in between "Brandell" and "Law" in the "Brandell Law" logo. Or a different font.

Industry/Entity Type

Legal

Font styles to use
Serif

Colors

Designer to choose only greyscale colors for use in the design.

Requirements
Must have
• The "Brandell Law" logo with the line in between "Brandell" and "Law" but I am open to ideas on structure and color schemes.
Nice to have
• Logo on top with new color scheme, along with my name and email.
• Address, phone number, web address on bottom.

```html
<!DOCTYPE html>
<html lang="en">
<head>
<meta charset="utf-8">
<title>Brandell Law PLLC – Letterhead</title>
<link href="https://fonts.googleapis.com/css2?family=Libre+Baskerville:wght@700&family=Montserrat:ital,wght@0,400;0,500;1,400&display=swap" rel="stylesheet">
<style>
  :root {
    --backdrop: #d3d3d3;
    --paper: #ffffff;
    --brand-blue: #2f5aa8;
    --ink: #3a3a3a;
    --ink-soft: #555555;
    --pattern-light: #f4f4f4;
    --pattern-mid: #e6e6e6;
  }
  * { margin: 0; padding: 0; box-sizing: border-box; }
  html, body {
    width: 1200px; height: 1200px; overflow: hidden;
    background: var(--backdrop);
  }
  .letterhead {
    position: absolute; left: 211px; top: 50px;
    width: 778px; height: 1100px;
    background: var(--paper);
    overflow: hidden;
    font-family: "Montserrat", Arial, sans-serif;
    color: var(--ink);
  }
  .pattern { position: absolute; }
  .pattern--top {
    right: 0; top: 0; width: 520px; height: 350px;
    background: radial-gradient(ellipse at top right, var(--pattern-mid) 0%, var(--pattern-light) 45%, rgba(255,255,255,0) 75%);
  }
  .pattern--bottom {
    left: 0; bottom: 0; width: 520px; height: 315px;
    background: radial-gradient(ellipse at bottom left, var(--pattern-mid) 0%, var(--pattern-light) 45%, rgba(255,255,255,0) 75%);
  }
  .brand-name {
    position: absolute; left: 75px; top: 40px;
    font-family: "Libre Baskerville", Georgia, serif;
    font-weight: 700; font-size: 33px; letter-spacing: 1px;
    color: var(--brand-blue);
    white-space: nowrap;
  }
  .sender {
    position: absolute; left: 78px; top: 109px;
    padding-left: 4px;
    border-left: 1.5px solid var(--brand-blue);
    font-size: 16px; line-height: 17.8px; letter-spacing: 0.4px;
    color: var(--ink-soft);
  }
  .salutation {
    position: absolute; left: 82px; top: 316px;
    font-style: italic; font-size: 15px; letter-spacing: 1.6px;
  }
  .letter-body {
    position: absolute; left: 78px; top: 354px;
    font-style: italic; font-size: 15px; line-height: 23.5px; letter-spacing: 2px;
    white-space: nowrap;
  }
  .contact-list {
    position: absolute; left: 76px; top: 960px;
    list-style: none;
    font-weight: 500; font-size: 18px; letter-spacing: 0.8px; color: var(--ink);
  }
  .contact-item {
    display: flex; align-items: flex-start; gap: 16px;
    line-height: 18px; margin-bottom: 9px;
  }
  .contact-icon {
    width: 22px; height: 22px; flex: none;
    background: var(--brand-blue);
    display: flex; align-items: center; justify-content: center;
  }
  .footer-brand {
    position: absolute; left: 506px; top: 1042px;
    font-family: "Libre Baskerville", Georgia, serif;
    font-weight: 700; font-size: 18px; letter-spacing: 1.5px;
    color: var(--ink);
    white-space: nowrap;
  }
</style>
</head>
<body>
  <main class="letterhead">
    <div class="pattern pattern--top" role="img" aria-label="Soft grey diamond tile pattern fading in from the top right corner"></div>
    <div class="pattern pattern--bottom" role="img" aria-label="Soft grey diamond tile pattern fading in from the bottom left corner"></div>

    <header>
      <div class="brand-name">BRANDELL | LAW</div>
      <div class="sender">
        <div>Douglas Brandell</div>
        <div>Brandell Law PLLC</div>
        <div>douglas@brandell-legal.example</div>
      </div>
    </header>

    <p class="salutation">Lorem ipsum</p>
    <div class="letter-body">
      <p>Lorem ipsumv dolor sit amet, consectetuer adipiscing elit, sed<br>
      diam nonummy nibh euismod tincidunt ut laoreet dolore magna<br>
      aliquam erat volutpat. Ut wisi enim ad minim veniam, quis<br>
      nostrud exerci tation ullamcorper suscipit lobortis nisl ut aliquip<br>
      ex ea commodo consequat. Duis autem vel eum iriure dolor in<br>
      hendrerit in vulputate velit esse molestie consequat, vel illum<br>
      dolore eu feugiat nulla facilisis at vero eros et accumsan et iusto<br>
      odio dignissim qui blandit praesent luptatum zzril delenit augue<br>
      duis dolore te feugait nulla facilisi.</p>
      <p>Lorem ipsum dolor sit amet, cons ectetuer adipiscing elit, sed<br>
      diam nonummy nibh euismod tincidunt ut laoreet dolore magna<br>
      aliquam erat volutpat. Ut wisi enim ad minim veniam, quis<br>
      nostrud exerci tation ullamcorper suscipit lobortis nisl ut aliquip<br>
      ex ea commodo consequat.</p>
      <p>&nbsp;&nbsp;Lorem ipsum dolor sit amet, consectetuer adipiscing elit, sed<br>
      diam nonummy nibh euismod tincidunt ut laoreet dolore magna</p>
    </div>

    <footer>
      <ul class="contact-list">
        <li class="contact-item">
          <span class="contact-icon"><svg width="13" height="13" viewBox="0 0 24 24"><path fill="#fff" d="M6.6 10.8a15 15 0 0 0 6.6 6.6l2.2-2.2a1 1 0 0 1 1-.25 11.4 11.4 0 0 0 3.6.57 1 1 0 0 1 1 1V20a1 1 0 0 1-1 1A17 17 0 0 1 3 4a1 1 0 0 1 1-1h3.5a1 1 0 0 1 1 1c0 1.25.2 2.45.57 3.6a1 1 0 0 1-.25 1z"/></svg></span>
          <span>214-555-0186</span>
        </li>
        <li class="contact-item">
          <span class="contact-icon"><svg width="12" height="14" viewBox="0 0 24 28"><path fill="#fff" d="M12 0a9 9 0 0 0-9 9c0 7 9 19 9 19s9-12 9-19a9 9 0 0 0-9-9zm0 12.5A3.5 3.5 0 1 1 12 5.5a3.5 3.5 0 0 1 0 7z"/></svg></span>
          <span>2750 Whitcombe, Suite 410<br>Dallas, Texas 75219</span>
        </li>
        <li class="contact-item">
          <span class="contact-icon"><svg width="13" height="13" viewBox="0 0 24 24"><circle cx="12" cy="12" r="9" fill="none" stroke="#fff" stroke-width="2"/><path d="M3 12h18M12 3c3 3 3 15 0 18M12 3c-3 3-3 15 0 18" fill="none" stroke="#fff" stroke-width="1.6"/></svg></span>
          <span>www.brandell-legal.example</span>
        </li>
      </ul>
      <div class="footer-brand">BRANDELL | LAW</div>
    </footer>
  </main>
</body>
</html>
```